Webdesign für KOR GmbH
Zielgruppe
KOR GmbH - Spezialist für Anlasser und Lichtmaschinen
Gegründet 1992 ist KOR nunmehr ein deutschlandweit agierendes Unternehmen mit 13 Mitarbeitern. Der Fokus unserer Arbeit liegt dabei auf der professionellen Regenerierung von Anlassern und Lichtmaschinen. Die strikte Arbeit nach Herstellerstandards und der hohe Anspruch an Qualität und Qualitätssicherung wurde durch die Einführung der ISO Zertifizierung 9001 untermauert.
Der Vertrieb von:
Anlassern
Lichtmaschinen
Turboladern
Klimakompressoren
Verdampfern / Kondensatoren
Batterien
namenhafter Hersteller ergänzt das Portfolio. Die Spezialisierung auf diese Produktgruppen ermöglicht dabei ein hohes Maß an Verfügbarkeit und marktgerechte Preise.
- Modern
- Klares und übersichtliches Desgin
- Nicht zu verspielt
- Informativ
- Leichte Navigation
- Das Design der alten Webseite soll NICHT kopiert werden
- Die Farben des Logos sollen sich wiederfinden

```html
<!DOCTYPE html>
<html lang="de">
<head>
<meta charset="utf-8">
<title>KOR GmbH – Spezialist für Anlasser & Lichtmaschinen</title>
<link href="https://fonts.googleapis.com/css2?family=Roboto:wght@400;500;700&display=swap" rel="stylesheet">
<style>
:root{
  --green:#12a05a;
  --green-dark:#0d8a4c;
  --white:#ffffff;
  --header-bg:#ffffff;
  --nav-bg:#3b3d40;
  --main-bg:#46484b;
  --footer-bg:#38393c;
  --text-light:#e6e7e8;
  --card-bg:#ffffff;
  --panel-bg:#f1f2f3;
  --input-border:#c8cacc;
}
*{margin:0;padding:0;box-sizing:border-box}
html,body{width:1200px;height:1132px;overflow:hidden}
body{font-family:"Roboto",Arial,sans-serif;background:var(--main-bg);position:relative;color:var(--text-light)}
.site-header{position:absolute;left:0;top:0;width:1200px;height:102px;background:var(--header-bg)}
.brand{position:absolute;left:89px;top:30px;display:flex;align-items:center;gap:10px;color:var(--green);font-weight:700;font-size:28px}
.brand-dot{width:14px;height:14px;border-radius:50%;background:var(--green)}
.header-note{position:absolute;right:65px;top:7px;font-size:11px;color:#666}
.header-links{position:absolute;right:142px;top:51px;font-size:12px;color:#555}
.header-shop{position:absolute;left:1067px;top:42px;width:68px;height:30px;background:var(--green);color:var(--white);font-size:14px;font-weight:500;display:flex;align-items:center;justify-content:center}
.main-nav{position:absolute;left:0;top:102px;width:1200px;height:53px;background:var(--nav-bg);display:flex;justify-content:center;gap:33px}
.main-nav a{color:var(--text-light);text-decoration:none;font-size:14px;line-height:53px;position:relative}
.main-nav a.active{color:var(--green)}
.main-nav a.active::after{content:"";position:absolute;left:-3px;right:-3px;bottom:0;height:3px;background:var(--green)}
.hero{position:absolute;left:0;top:155px;width:1200px;height:317px;
  background:
    radial-gradient(ellipse 30% 40% at 72% 45%,rgba(120,124,130,.55),transparent 70%),
    radial-gradient(ellipse 35% 45% at 28% 50%,rgba(95,100,108,.5),transparent 70%),
    radial-gradient(ellipse 60% 70% at 50% 35%,#4a4d52 0%,#2a2c2f 60%,#17181a 100%);
  text-align:center}
.hero-title{position:absolute;left:0;right:0;top:148px;font-size:29px;font-weight:700;color:var(--white)}
.hero-sub{position:absolute;left:0;right:0;top:186px;font-size:17px;color:var(--white)}
.hero-btn{position:absolute;left:560px;top:223px;width:100px;height:31px;background:var(--green);color:var(--white);font-size:14px;font-weight:500;display:flex;align-items:center;justify-content:center}
.side{position:absolute;left:63px;top:519px;width:316px}
.photo{height:132px;background:
  linear-gradient(180deg,#eef2f5 0%,#dfe6ea 38%,#b9c2c8 62%,#c9cfd3 100%)}
.section-title{font-size:22px;font-weight:700;color:var(--white)}
.side .section-title.company{margin-top:16px}
.side p{margin-top:22px;font-size:13px;line-height:20px;color:var(--text-light)}
.side .section-title.shop{margin-top:28px}
.contact-panel{margin-top:20px;height:190px;background:var(--panel-bg);padding:12px 12px 0;position:relative}
.field{height:22px;border:1px solid var(--input-border);background:#fff;font-size:11px;color:#666;padding:3px 6px;margin-bottom:6px}
.field-label{font-size:10px;color:#777;margin:0 0 4px 4px}
.toggles{display:flex;gap:6px;align-items:center;font-size:10px;color:#777;margin:2px 0 8px 4px}
.toggle{width:12px;height:12px;border-radius:3px;background:#3b82f6}
.toggle.off{background:#bbb}
.map{position:absolute;left:0;right:0;bottom:0;height:52px;background:linear-gradient(100deg,#dfe8da 0%,#eceee9 45%,#e4e6e2 100%)}
.content{position:absolute;left:409px;top:519px;width:727px}
.cards{display:flex;gap:17px;margin-top:20px}
.card{flex:1;height:168px;background:var(--card-bg);overflow:hidden}
.card-img{height:121px;background:radial-gradient(circle at 50% 52%,#f4f5f6 0%,#b8bcc0 30%,#7e8489 55%,#e3e5e6 100%)}
.card-img.warm{background:radial-gradient(circle at 55% 52%,#f1f2f3 0%,#a9adb1 30%,#5f6a78 55%,#c9a63a 100%)}
.card-label{padding:6px 7px;font-size:12px;line-height:15px;color:var(--green-dark);font-weight:500}
.content .section-title.repair{margin-top:56px}
.content p{margin-top:26px;font-size:13px;line-height:20px;color:var(--text-light)}
.site-footer{position:absolute;left:0;top:1085px;width:1200px;height:47px;background:var(--footer-bg)}
.site-footer a{position:absolute;top:16px;font-size:14px;color:var(--green);text-decoration:none}
</style>
</head>
<body>
<header class="site-header">
  <div class="brand"><span class="brand-dot"></span>KOR GmbH</div>
  <div class="header-note">KOR Service – ISO 9001 seit 1992</div>
  <div class="header-links">Unternehmen · Service</div>
  <a class="header-shop">Shop</a>
</header>
<nav class="main-nav">
  <a class="active">Unternehmen</a><a>Mitarbeiter</a><a>Prüfstände</a><a>Lager</a><a>Produkte</a><a>Instandsetzung</a><a>Kontakt</a><a>Shop</a>
</nav>
<section class="hero" role="img" aria-label="Geöffneter Motorraum eines Autos">
  <h1 class="hero-title">KOR GmbH - Spezialist für Anlaser &amp; Lichtmashinen</h1>
  <div class="hero-sub">Qualität seit 1992</div>
  <a class="hero-btn">Zum Shop</a>
</section>
<aside class="side">
  <div class="photo" role="img" aria-label="Helle Werkstatthalle mit Arbeitsplätzen"></div>
  <h2 class="section-title company">Unternehmen</h2>
  <p>KOR GmbH ISO 9001 zertifiziert mit bundesweitem Vertrieb nach strengen Herstellerstandards und 13 Mitarbeitern im Team.</p>
  <h2 class="section-title shop">Shop</h2>
  <div class="contact-panel">
    <div class="field">Name</div>
    <div class="field-label">E-Mail</div>
    <div class="field">Nachricht</div>
    <div class="field-label">Rückruf</div>
    <div class="toggles"><span class="toggle"></span><span class="toggle off"></span>Absenden</div>
    <div class="map" role="img" aria-label="Straßenkarte mit Standortmarkierung"></div>
  </div>
</aside>
<main class="content">
  <h2 class="section-title">Produkte</h2>
  <div class="cards">
    <div class="card"><div class="card-img" role="img" aria-label="Anlasser"></div><div class="card-label">Anlasser</div></div>
    <div class="card"><div class="card-img" role="img" aria-label="Lichtmaschine"></div><div class="card-label">Anlasser<br>Lichtmaschinen</div></div>
    <div class="card"><div class="card-img" role="img" aria-label="Klimakompressor"></div><div class="card-label">Klimakompressoren &amp;<br>Klimazubehör</div></div>
    <div class="card"><div class="card-img warm" role="img" aria-label="Turbolader"></div><div class="card-label">Verdampfer/<wbr>Kondensatoren<br>Turbolader</div></div>
  </div>
  <h2 class="section-title repair">Instandsetzung</h2>
  <p>Die KOR GmbH ist Ihr Ansprechpartner für die professionelle Regenerierung von Anlassern und Lichtmaschinen. Wir arbeiten nach Herstellerstandards und sichern jede Instandsetzung durch geprüfte Abläufe, moderne Prüfstände und erfahrene Mitarbeiter ab.</p>
</main>
<footer class="site-footer">
  <a style="left:63px">AGB</a>
  <a style="left:136px">Impressum</a>
  <a style="left:253px">Datenschutz</a>
  <a style="left:363px">Download</a>
  <a style="left:469px">BFSG</a>
</footer>
</body>
</html>
```